Beauty Salon Industry - Web Design Project

zQuarta is a well-funded start up developing an Online Marketing Platform for small businesses in Europe.
We require a large number of high quality business web designs for our business website builder. Our business websites are seamlessly integrated into our Online Marketing systems and therefore it is important for designers to comply with our Design Guidelines.
This is our second contest and it will focus on the beauty salon industry. We will be running contents every 2-3 weeks for a new industry. Last month, we ran a contest for Builder website designs with 3 top prizes (plus £10 per variation) and we also paid out £25 per design for 20+ entries from designers who did not win the top prizes. So we encourage all entries!
We have included a wire frame this time to encourage you to be as creative as possible with your designs and layout while respecting the following guidelines:
1) You CAN change the layout as much as you like. If you think a vertical menu would look better, then use it. If you think the design would benefit from moving an element to a different location, then you can do that too.
2) You must include ALL the elements in the wire frame in your design.(e.g. latest 2 news entries, a testimonial, 1 gallery image, carousel etc...). Please make sure you have looked through the wire frame and know what is required. Entries that do not include all the elements will not qualify to win.
3) So remember, you CAN change the layout as much as you like but DO NOT remove any elements nor move them to a different page.
4) You may change the size and style of the carousel image. We would like to see as many variations of this as possible.
We are rewarding 3 prizes, and would like the winning designer to design the internal pages to the new design.
As always, if we think your designs could be incorporated into our system, but you do not win the competition, we will reward £25. Therefore, we encourage designers to submit as many designs as possible as we may award up to 25 designs.
Judging criteria : -
1) Visual Design
2) Layout must adhere to best practices and wireframe. If you decide to move elements around significantly please provide reason
3) Functional, informative and drives calls to action
Updates
As usual:
1st place = £350
2nd place = £250
3rd place = £150
Good luck!
Very happy with all the designs submitted so far, and will provide feedback ASAP.
We would like to see you try arranging the elements differently. So please try different navigation types and layouts.
Thanks
Morris
Prize funds for 1st place has been slightly increased.
Thanks
Morris
We have already had some amazing designs submitted. Thanks.
Remember to play with the layout of the elements and try designs with a carousel/slider that is in portrait not just in landscape.
Thanks everyone!
Morris
Hi everyone, we are really enjoying looking through the designs.
We have one NEW requirement. If you have used an image from http://www.frelik-example.com/ in your design, could you please replace it with another.
We are not associated with them.
Thank you.
I have just sent a poll around the office to vote on all the designs and hope to have the results soon.
Good luck and I hope to see all your great designs for our next project in a couple of weeks.
Morris
Hi everyone, we hope you have had a good holiday season. We will be rewarding the prizes very soon, hopefully today or tomorrow.
Thanks
Morris
We are currently going through all the designs that did not win our competition and will be contacting the designers of the designs we would like to use in our system, so please keep an eye on your inbox over the next few days.
Thank you
Morris
Target Market(s)
Beauty Salon Industry
Industry/Entity Type
Beauty Salon
Look and feel
Each slider illustrates characteristics of the customer's brand and the style your logo design should communicate.

```html
<!DOCTYPE html>
<html lang="en">
<head>
<meta charset="utf-8">
<title>Silk Strand – Hair and Urban Spa</title>
<link href="https://fonts.googleapis.com/css2?family=Ubuntu:wght@300;400;500&family=Arimo:wght@400&display=swap" rel="stylesheet">
<style>
:root{
  --page-bg:#eeeeee;
  --panel:#ffffff;
  --green:#84cf1e;
  --blue:#47b4e4;
  --blue-light:#a6ddf5;
  --blue-fold:#7ecbe9;
  --yellow:#f5c40f;
  --text:#555555;
  --text-soft:#8a8a8a;
  --line:#dddddd;
  --band:#efefef;
}
*{margin:0;padding:0;box-sizing:border-box}
html,body{width:1200px;height:857px;overflow:hidden;background:var(--page-bg)}
body{position:relative;font-family:"Arimo",Arial,sans-serif;color:var(--text)}
h2,h3{font-weight:300}
.abs{position:absolute}
.panel{left:140px;top:0;width:915px;height:857px;background:var(--panel)}

/* header */
.logo{left:171px;top:18px;display:flex;align-items:center;gap:6px}
.logo-dot{width:24px;height:24px;border-radius:50%;background:var(--green)}
.logo-name{font-family:"Ubuntu",sans-serif;font-size:21px;color:var(--blue-light);line-height:1}
.logo-tag{left:201px;top:52px;font-family:"Ubuntu",sans-serif;font-size:9px;color:#555}
.header-rule{left:140px;top:71px;width:775px;height:1px;background:#e8e8e8}
.header-divider{left:316px;top:0;width:1px;height:71px;background:#e8e8e8}
.nav{left:326px;top:32px;display:flex;font-family:"Ubuntu",sans-serif;font-size:13px;color:#555}
.nav a{color:inherit;text-decoration:none;padding:5px 14px;border-radius:13px}
.nav a.active{background:var(--green);color:#fff}
.call-box{left:917px;top:0;width:165px;height:97px;background:var(--blue-light);border-radius:0 0 6px 6px}
.call-fold{left:1056px;top:97px;width:0;height:0;border-top:22px solid var(--blue-fold);border-right:26px solid transparent}
.phone{left:926px;top:17px;display:flex;align-items:center;gap:5px;font-family:"Ubuntu",sans-serif;font-size:18px;color:#fff}
.book-now{left:939px;top:52px;width:121px;height:30px;border-radius:15px;background:var(--yellow);color:#fff;font-family:"Ubuntu",sans-serif;font-size:15px;text-align:center;line-height:30px}

/* intro */
.bullet{width:12px;height:12px;border-radius:50%;background:var(--green)}
.section-title{font-family:"Ubuntu",sans-serif;font-size:15.5px;color:#444;line-height:15px}
.intro-text{left:188px;top:138px;width:165px;font-size:8.6px;line-height:15.4px;color:var(--text-soft)}
.intro-text p+p{margin-top:15px}
.more-btn{left:187px;top:374px;width:40px;height:19px;border-radius:10px;background:var(--blue-light)}
.scissors-art{left:90px;top:161px;width:56px;height:106px;background:radial-gradient(ellipse at center,rgba(90,90,90,.18),rgba(90,90,90,0) 70%)}

/* hero */
.hero{left:375px;top:97px;width:450px;height:296px;border-radius:10px;background:linear-gradient(120deg,#dfe6ea 0%,#c9b7a2 45%,#9b6e4f 60%,#e8eef1 100%)}
.hero-shadow{left:380px;top:408px;width:440px;height:30px;border-radius:50%;background:radial-gradient(ellipse at center,rgba(0,0,0,.12),rgba(0,0,0,0) 70%)}
.dots{left:805px;top:126px;width:25px;height:70px;background:#fff;border-radius:12px 0 0 12px}
.dot{width:13px;height:13px;border-radius:50%;border:1px solid #bbb;background:#fff}
.dot.on{background:var(--green);border-color:var(--green)}

/* promo */
.promo-photo{left:825px;top:120px;width:118px;height:163px;background:linear-gradient(160deg,#f2e4dc,#7a4a35 50%,#f3ebe7);border-radius:0 0 0 40px}
.price{left:950px;top:148px;font-family:"Ubuntu",sans-serif;font-weight:300;font-size:48px;color:var(--green);line-height:1}
.price small{font-size:20px}
.promo-line1{left:847px;top:283px;font-family:"Ubuntu",sans-serif;font-size:15px;color:var(--green);text-decoration:underline}
.promo-line2{left:847px;top:306px;font-family:"Ubuntu",sans-serif;font-size:16px;color:var(--green)}
.appt-btn{left:845px;top:340px;width:154px;height:31px;border-radius:8px;background:var(--green);color:#fff;font-family:"Ubuntu",sans-serif;font-size:13px;text-align:center;line-height:31px}
.cut-line{left:824px;top:439px;width:230px;border-top:2px dashed #333}
.scissors-right{left:990px;top:373px;width:116px;height:77px;background:radial-gradient(ellipse at center,rgba(90,90,90,.18),rgba(90,90,90,0) 70%)}

/* hours */
.hours-title{left:915px;top:466px;font-family:"Ubuntu",sans-serif;font-weight:400;font-size:15px;color:#555}
.hours{left:915px;top:490px;font-family:"Ubuntu",sans-serif;font-size:10px;color:#666}
.hours div{height:21.3px;display:flex;align-items:center}
.hours b{font-weight:300;font-size:13.5px;color:var(--green);width:37px}

/* gallery */
.gallery-photo{left:187px;top:470px;width:157px;height:125px;border-radius:8px;background:linear-gradient(135deg,#8d6e57,#d9b98f 50%,#5a5a5a)}
.gallery-btn{left:213px;top:579px;width:105px;height:31px;border-radius:10px;background:var(--blue-light);color:#3a9fcf;font-family:"Ubuntu",sans-serif;font-size:14px;text-align:center;line-height:31px}

/* testimonial */
.testimonial{left:375px;top:446px;width:450px;height:86px;background:#fff;border-radius:8px;box-shadow:0 2px 3px rgba(0,0,0,.12)}
.quote-mark{font-family:"Ubuntu",sans-serif;font-size:34px;color:var(--blue-light);line-height:1}
.quote-text{left:420px;top:455px;width:370px;font-size:8.6px;line-height:15.5px;color:#555}
.quote-author{left:420px;top:505px;font-family:"Ubuntu",sans-serif;font-size:11.5px;color:var(--blue)}
.pager{left:694px;top:514px;display:flex;gap:8px}
.pager span{width:17px;height:17px;border-radius:50%;border:1px solid #ccc;font-family:"Ubuntu",sans-serif;font-size:10px;text-align:center;line-height:16px;color:#555}
.pager span.on{color:var(--blue);border-color:var(--blue-light)}

/* news */
.news-item{width:180px}
.news-title{font-family:"Ubuntu",sans-serif;font-size:11.5px;line-height:15.5px;color:var(--green)}
.news-date{font-family:"Ubuntu",sans-serif;font-size:8.6px;color:#555;margin-top:10px}
.news-divider{left:606px;top:549px;width:1px;height:63px;background:var(--line)}

/* partners */
.partners{left:187px;top:638px;width:868px;height:103px;background:var(--band);border-radius:10px 0 0 10px;display:flex}
.partner{display:flex;align-items:center;justify-content:center;border-right:1px solid #fff;font-family:"Ubuntu",sans-serif;font-weight:500;font-size:24px;color:#333}
.rollers{left:968px;top:716px;width:80px;height:55px;background:radial-gradient(ellipse at center,rgba(60,190,110,.35),rgba(60,190,110,0) 70%)}

/* footer */
.footer-nav{left:188px;top:760px;font-family:"Ubuntu",sans-serif;font-size:9.5px;color:#555}
.footer-nav span{color:#999;margin:0 8px}
.managed{left:807px;top:760px;font-family:"Ubuntu",sans-serif;font-size:9px;color:#555}
.admin-btn{left:933px;top:782px;width:98px;height:30px;border-radius:8px;background:var(--yellow);color:#fff;font-family:"Ubuntu",sans-serif;font-size:14px;text-align:center;line-height:30px}
</style>
</head>
<body>
<div class="abs panel"></div>

<header>
  <div class="abs logo"><span class="logo-dot"></span><span class="logo-name">Silk Strand</span></div>
  <div class="abs logo-tag">Hair and Urban Spa</div>
  <div class="abs header-divider"></div>
  <div class="abs header-rule"></div>
  <nav class="abs nav">
    <a href="#">Home</a><a href="#">Services</a><a href="#" class="active">Gallery</a><a href="#">Testimonials</a><a href="#">News</a><a href="#">About Us</a><a href="#">Contact Us</a>
  </nav>
  <div class="abs call-box"></div>
  <div class="abs call-fold"></div>
  <div class="abs phone">
    <svg width="22" height="22" viewBox="0 0 24 24" aria-hidden="true"><path d="M6 3h4l2 5-2.5 1.5a11 11 0 0 0 5 5L16 12l5 2v4a2 2 0 0 1-2 2A16 16 0 0 1 4 5a2 2 0 0 1 2-2z" fill="none" stroke="#fff" stroke-width="1.6"/></svg>
    020 7946 0812
  </div>
  <div class="abs book-now">Book Now !</div>
</header>

<main>
  <div class="abs bullet" style="left:161px;top:103px"></div>
  <h2 class="abs section-title" style="left:187px;top:101px">Let Our Hair and Beauty<br>Skills Blow you Away !</h2>
  <div class="abs intro-text">
    <p>It is a long established fact that a reader will be distracted by the readable content of a page when looking at its layout. The point of using Lorem Ipsum is that it has a more-or-less normal distribution of letters, as opposed to using 'Content here, content here',</p>
    <p>making it look like readable English. Many desktop publishing packages and web page editors now use Lorem Ipsum as their default model text, and a search for 'lorem ipsum' will uncover many web sites still in their infancy.</p>
  </div>
  <div class="abs more-btn"><svg width="40" height="19" viewBox="0 0 40 19" aria-hidden="true"><path d="M14 9.5h12m-3-3 3 3-3 3" stroke="#fff" stroke-width="1.2" fill="none"/></svg></div>
  <div class="abs scissors-art" role="img" aria-label="Decorative pair of scissors"></div>

  <div class="abs hero" role="img" aria-label="Slider photo of a smiling woman with curly hair"></div>
  <div class="abs dots">
    <div class="abs dot on" style="left:6px;top:8px"></div>
    <div class="abs dot" style="left:6px;top:30px"></div>
    <div class="abs dot" style="left:6px;top:52px"></div>
  </div>
  <div class="abs hero-shadow"></div>

  <div class="abs promo-photo" role="img" aria-label="Photo of a woman with long straight hair"></div>
  <svg class="abs" style="left:930px;top:125px" width="115" height="190" viewBox="0 0 115 190" aria-hidden="true">
    <circle cx="54" cy="55" r="47" fill="none" stroke="#84cf1e" stroke-width="3" stroke-dasharray="4 6" stroke-linecap="round"/>
    <path d="M78 110c22 20 14 40-6 55l-12 8" fill="none" stroke="#84cf1e" stroke-width="2" stroke-dasharray="4 5" stroke-linecap="round"/>
  </svg>
  <div class="abs price">25<small>£</small></div>
  <div class="abs promo-line1">Compliminatry Gift</div>
  <div class="abs promo-line2">for first time client!</div>
  <div class="abs appt-btn">Book Appointment Now</div>
  <div class="abs cut-line"></div>
  <div class="abs scissors-right" role="img" aria-label="Decorative open scissors"></div>

  <svg class="abs" style="left:848px;top:455px" width="54" height="54" viewBox="0 0 54 54" aria-hidden="true">
    <circle cx="27" cy="27" r="26" fill="#111"/><circle cx="27" cy="27" r="19" fill="#fff"/>
    <path d="M27 14v13h10" stroke="#111" stroke-width="5" fill="none"/>
  </svg>
  <h3 class="abs hours-title">Buisness Time</h3>
  <div class="abs hours">
    <div><b>Mon.</b>9 a.m - 5 p.m</div>
    <div><b>Tue.</b>9 a.m - 5 p.m</div>
    <div><b>Wed.</b>9 a.m - 5 p.m</div>
    <div><b>Thu.</b>9 a.m - 5 p.m</div>
    <div><b>Fri.</b>9 a.m - 5 p.m</div>
    <div><b>Sat.</b>9 a.m - 5 p.m</div>
  </div>

  <div class="abs bullet" style="left:161px;top:444px"></div>
  <h2 class="abs section-title" style="left:187px;top:443px">Gallery</h2>
  <div class="abs gallery-photo" role="img" aria-label="Gallery photo of a stylist colouring a client's hair"></div>
  <div class="abs gallery-btn">View Gallery</div>

  <div class="abs testimonial"></div>
  <div class="abs quote-mark" style="left:386px;top:448px">“</div>
  <div class="abs quote-mark" style="left:787px;top:480px">”</div>
  <p class="abs quote-text">There are many variations of passages of Lorem Ipsum available, but the majority have suffered alteration in some form, by injected humour, or randomised words which don't look even slightly believable. If you are going to use a passage of Lorem Ipsum,</p>
  <div class="abs quote-author">- Elena Marsh</div>
  <div class="abs pager"><span class="on">1</span><span>2</span><span>3</span></div>

  <svg class="abs" style="left:397px;top:552px" width="15" height="13" viewBox="0 0 15 13" aria-hidden="true"><path d="M1 1h9v6H5l-3 2V7H1zM10 4h4v6h-1v2l-3-2H6V7" fill="none" stroke="#999"/></svg>
  <div class="abs news-item" style="left:425px;top:555px">
    <div class="news-title">But I must explain to you how all this mistaken idea</div>
    <div class="news-date">12 Dec,2011</div>
  </div>
  <svg class="abs" style="left:546px;top:590px" width="14" height="8" viewBox="0 0 14 8" aria-hidden="true"><path d="M0 4h13M10 1l3 3-3 3" stroke="#84cf1e" fill="none"/></svg>
  <div class="abs news-divider"></div>
  <svg class="abs" style="left:636px;top:552px" width="15" height="13" viewBox="0 0 15 13" aria-hidden="true"><path d="M1 1h9v6H5l-3 2V7H1zM10 4h4v6h-1v2l-3-2H6V7" fill="none" stroke="#999"/></svg>
  <div class="abs news-item" style="left:663px;top:555px">
    <div class="news-title">But I must explain to you how all this mistaken idea</div>
    <div class="news-date">12 Dec,2011</div>
  </div>
  <svg class="abs" style="left:784px;top:590px" width="14" height="8" viewBox="0 0 14 8" aria-hidden="true"><path d="M0 4h13M10 1l3 3-3 3" stroke="#84cf1e" fill="none"/></svg>

  <div class="abs partners">
    <div class="partner" style="width:215px">Lumena</div>
    <div class="partner" style="width:292px">Verdelle</div>
    <div class="partner" style="width:234px">Haarwerk</div>
    <div style="flex:1"></div>
  </div>
  <div class="abs rollers" role="img" aria-label="Hair rollers and a round brush"></div>
</main>

<footer>
  <div class="abs footer-nav">Home<span>|</span>Services<span>|</span>Gallery<span>|</span>Testimonials<span>|</span>News<span>|</span>About Us<span>|</span>Contact Us</div>
  <div class="abs managed">Managed by zQuarta.com</div>
  <div class="abs admin-btn">Admin</div>
</footer>
</body>
</html>
```